Dovrantiquell

We need a book cover for an upcoming book publication. Please see attachment for the text that should go on the book cover. We want a sleek and impacting design, but not overly busy. The target industry is oral-maxillofacial. Thanks and good luck!

```html
<!DOCTYPE html>
<html lang="en">
<head>
<meta charset="utf-8">
<title>Dovrantiquell — Book Cover</title>
<link rel="stylesheet" href="https://fonts.googleapis.com/css2?family=Montserrat:wght@800&family=Quicksand:wght@400;500&display=swap">
<style>
  :root {
    --page-bg: #ece9e4;
    --ink-black: #0b0b0b;
    --spine-black: #111111;
    --band-light: #e4e4e4;
    --band-light-edge: #cfcfcf;
    --def-grey: #6e6e6e;
    --def-grey-dark: #5c5c5c;
    --def-text: #ededed;
    --xray-deep: #05070d;
    --xray-mid: #1c2a4a;
    --xray-glow: #5f7bb0;
    --footer-text: #d8d8d8;
  }
  * { margin: 0; padding: 0; box-sizing: border-box; }
  html, body {
    width: 1200px; height: 1000px; overflow: hidden;
    background: var(--page-bg);
  }
  .book {
    position: absolute; left: 285px; top: 30px;
    width: 630px; height: 940px;
    display: flex;
    box-shadow: 0 6px 24px rgba(0,0,0,0.18);
  }
  .spine {
    width: 40px; height: 100%;
    background: var(--spine-black);
    position: relative;
  }
  .spine-title {
    position: absolute; left: 50%; top: 690px;
    transform: translate(-50%, -50%) rotate(-90deg);
    font-family: "Montserrat", sans-serif; font-weight: 800;
    font-size: 22px; letter-spacing: 1px; color: #f2f2f2;
    white-space: nowrap;
  }
  .spine-author {
    position: absolute; left: 50%; top: 170px;
    transform: translate(-50%, -50%) rotate(90deg);
    font-family: "Quicksand", sans-serif; font-size: 10px;
    color: #bdbdbd; white-space: nowrap;
  }
  .cover {
    width: 590px; height: 100%;
    display: flex; flex-direction: column;
  }
  .cover-art {
    height: 438px;
    background:
      radial-gradient(ellipse 55% 60% at 55% 55%, var(--xray-glow) 0%, var(--xray-mid) 45%, transparent 80%),
      radial-gradient(ellipse 40% 50% at 20% 35%, #2b3d66 0%, transparent 70%),
      var(--xray-deep);
  }
  .title-band {
    height: 191px;
    background: linear-gradient(180deg, var(--band-light) 0%, #dcdcdc 100%);
    border-bottom: 2px solid var(--band-light-edge);
    padding: 52px 22px 0 0;
    text-align: right;
  }
  .book-title {
    font-family: "Montserrat", sans-serif; font-weight: 800;
    font-size: 49px; line-height: 1; color: var(--ink-black);
    letter-spacing: 0.5px;
  }
  .book-author {
    margin-top: 18px; margin-right: 2px;
    font-family: "Quicksand", sans-serif; font-weight: 500;
    font-size: 15px; color: #222;
  }
  .definition-panel {
    height: 211px;
    background: linear-gradient(180deg, var(--def-grey) 0%, var(--def-grey-dark) 100%);
    display: flex;
  }
  .definition-art {
    width: 125px; height: 100%;
    background: linear-gradient(90deg, #9aa0a8 0%, #7c8087 60%, var(--def-grey) 100%);
    opacity: 0.85;
  }
  .definition {
    padding: 30px 20px 0 16px;
    font-family: "Quicksand", sans-serif; font-weight: 500;
    color: var(--def-text); font-size: 13px; line-height: 1.35;
  }
  .definition-head { margin-bottom: 16px; }
  .sense { display: flex; gap: 12px; margin-bottom: 14px; }
  .sense-num { width: 14px; flex: none; }
  .cover-footer {
    flex: 1;
    background: var(--ink-black);
    padding: 44px 0 0 12px;
    font-family: "Quicksand", sans-serif; font-size: 13px;
    color: var(--footer-text);
  }
</style>
</head>
<body>
  <div class="book">
    <div class="spine">
      <span class="spine-author">Name of the author</span>
      <span class="spine-title">DOVRANTIQUELL</span>
    </div>
    <div class="cover">
      <div class="cover-art" role="img" aria-label="Blue translucent X-ray style render of a human skull in side profile showing jaw and teeth"></div>
      <div class="title-band">
        <h1 class="book-title">DOVRANTIQUELL</h1>
        <p class="book-author">Name of the author</p>
      </div>
      <div class="definition-panel">
        <div class="definition-art" role="img" aria-label="Faint greyscale X-ray detail of the cervical spine"></div>
        <div class="definition">
          <p class="definition-head">noun &nbsp;|&nbsp; \ dov - ran - ti - quell \</p>
          <p class="sense"><span class="sense-num">1 :</span><span>the practice of clinical aesthetics with medical-grade products.</span></p>
          <p class="sense"><span class="sense-num">2 :</span><span>a universal clinical perception of natural geometric forms and height of contours.</span></p>
          <p class="sense"><span class="sense-num">3 :</span><span>aesthetic diagnosis and treatment knowledgebase.</span></p>
        </div>
      </div>
      <div class="cover-footer">Editor/Year</div>
    </div>
  </div>
</body>
</html>
```